Business Card Design

My company is a Consulting & Training company (Halvorn Consulting and Training, LLC) specializing in Firearms Training, State of Florida Concealed Weapons Permit Course, and Tactical Equipment Consulting.

Industry/Entity Type

Business

Contact Information for Business Card

Tobin Halvorn
P.O. Box 412763
Aventura, FL 33197
(786)555-0148

```html
<!DOCTYPE html>
<html lang="en">
<head>
<meta charset="utf-8">
<title>Halvorn Consulting &amp; Training — Business Card</title>
<link rel="stylesheet" href="https://fonts.googleapis.com/css2?family=Raleway:wght@400;500;600&display=swap">
<style>
  :root {
    --backdrop: #d4d4d4;
    --card: #2e3035;
    --card-line: #34363b;
    --brand-blue: #3f7fd0;
    --name-white: #f2f2f2;
    --name-grey: #b9bbbf;
    --detail: #d6d7da;
  }
  * { margin: 0; padding: 0; box-sizing: border-box; }
  html, body {
    width: 1200px;
    height: 900px;
    overflow: hidden;
    background: var(--backdrop);
    font-family: "Raleway", sans-serif;
  }
  .canvas {
    position: relative;
    width: 1200px;
    height: 900px;
  }
  .card {
    position: absolute;
    border-radius: 16px;
    background-color: var(--card);
    background-image: repeating-linear-gradient(90deg, transparent 0 2px, var(--card-line) 2px 3px);
    overflow: hidden;
  }
  .card--front { left: 311px; top: 59px; width: 604px; height: 351px; }
  .card--back  { left: 311px; top: 462px; width: 601px; height: 349px; }

  .wordmark {
    position: absolute;
    display: flex;
    align-items: center;
    justify-content: center;
    color: var(--brand-blue);
    font-weight: 600;
    text-transform: uppercase;
    white-space: nowrap;
  }
  .wordmark__name span { display: block; }
  .wordmark__dot {
    flex: none;
    border-radius: 50%;
    background: var(--brand-blue);
  }
  .card--front .wordmark {
    left: 0; width: 100%; top: 130px; gap: 16px;
    font-size: 22px; line-height: 1.35; letter-spacing: 0.06em;
  }
  .card--front .wordmark__dot { width: 20px; height: 20px; }
  .card--back .wordmark {
    left: 30px; width: 260px; top: 142px; gap: 10px;
    font-size: 15px; line-height: 1.35; letter-spacing: 0.05em;
  }
  .card--back .wordmark__dot { width: 13px; height: 13px; }

  .contact {
    position: absolute;
    left: 301px;
    top: 128px;
  }
  .contact__name {
    font-size: 29px;
    font-weight: 400;
    line-height: 1;
    color: var(--name-grey);
    letter-spacing: 0.01em;
  }
  .contact__name .first { color: var(--name-white); }
  .contact__role {
    margin-top: 7px;
    font-size: 15px;
    color: var(--brand-blue);
  }
  .contact__details {
    margin-top: 16px;
    margin-left: 4px;
    list-style: none;
    font-size: 15.5px;
    line-height: 21px;
    color: var(--detail);
  }
</style>
</head>
<body>
  <main class="canvas">
    <section class="card card--front" aria-label="Card front">
      <div class="wordmark">
        <span class="wordmark__dot"></span>
        <span class="wordmark__name"><span>Halvorn</span><span>Consulting &amp; Training</span></span>
      </div>
    </section>

    <section class="card card--back" aria-label="Card back">
      <div class="wordmark">
        <span class="wordmark__dot"></span>
        <span class="wordmark__name"><span>Halvorn</span><span>Consulting &amp; Training</span></span>
      </div>
      <div class="contact">
        <h1 class="contact__name"><span class="first">Tobin</span> Halvorn</h1>
        <p class="contact__role">Managing Director</p>
        <ul class="contact__details">
          <li>P.O. Box 412763</li>
          <li>Aventura, FL 33197</li>
          <li>(786)555-0148</li>
        </ul>
      </div>
    </section>
  </main>
</body>
</html>
```